Quilvo Garage Doors Business Card

I need a Business Card for my garage door business:
Quilvo Garage Doors.
please add:
logo
phone number: 855-3-QUILVO
(853-392)

email: service@quilvogaragedoors.com
website: www.quilvogaragedoors.com

The attached image is recommendation ONLY.

```html
<!DOCTYPE html>
<html lang="en">
<head>
<meta charset="utf-8">
<title>Quilvo Garage Doors – Business Card</title>
<link href="https://fonts.googleapis.com/css2?family=Quicksand:wght@400;500;600;700&display=swap" rel="stylesheet">
<style>
  :root {
    --page: #2b2b2d;
    --card-dark: #2e2c2e;
    --card-dark-edge: #3a383a;
    --card-light: #f4f5f5;
    --teal: #5bb8c1;
    --ink: #333335;
    --ink-soft: #c9c9cb;
    --white: #ffffff;
  }
  * { margin: 0; padding: 0; box-sizing: border-box; }
  html, body {
    width: 1200px; height: 900px; overflow: hidden;
    background: var(--page);
    font-family: "Quicksand", sans-serif;
  }
  .canvas {
    position: relative; width: 1200px; height: 900px;
    display: flex; flex-direction: column; align-items: center; justify-content: center; gap: 60px;
  }
  .card {
    position: relative; width: 630px; height: 360px; overflow: hidden;
    box-shadow: 0 14px 40px rgba(0,0,0,.45);
  }

  /* Back side */
  .card-back {
    background: linear-gradient(160deg, var(--card-dark-edge), var(--card-dark) 60%);
    display: flex; align-items: center; justify-content: center;
  }
  .brand { display: flex; align-items: center; gap: 18px; }
  .brand-mark { width: 54px; height: 54px; background: var(--teal); border-radius: 8px; }
  .brand-name { font-weight: 600; font-size: 34px; line-height: 1.1; color: var(--ink-soft); }
  .card-back .brand-name { color: var(--ink-soft); }

  /* Front side */
  .card-front { background: var(--card-light); }
  .front-top {
    position: absolute; left: 0; top: 0; width: 100%; height: 200px;
    padding: 0 44px; display: flex; align-items: center; justify-content: space-between;
  }
  .card-front .brand-mark { width: 46px; height: 46px; }
  .card-front .brand-name { font-size: 28px; color: var(--ink); }
  .person { align-self: flex-start; margin-top: 44px; text-align: left; }
  .person-name { color: var(--teal); font-weight: 600; font-size: 20px; letter-spacing: 1px; text-transform: uppercase; }
  .person-role { color: var(--ink); font-weight: 500; font-size: 15px; margin-top: 2px; padding-left: 30px; }

  .front-bottom {
    position: absolute; left: 0; top: 200px; width: 100%; height: 160px;
    background: linear-gradient(160deg, var(--card-dark-edge), var(--card-dark) 60%);
  }
  .contact-list {
    list-style: none; position: absolute; left: 44px; top: 38px;
    display: flex; flex-direction: column; gap: 7px;
  }
  .contact-item { display: flex; align-items: center; gap: 10px; color: var(--ink-soft); font-size: 15px; font-weight: 500; }
  .contact-icon { width: 18px; height: 18px; flex: none; }
  .accent-stripe {
    position: absolute; left: 0; bottom: 22px; width: 100%; height: 18px; background: var(--teal);
  }
</style>
</head>
<body>
<main class="canvas">
  <section class="card card-back" aria-label="Business card back">
    <div class="brand">
      <span class="brand-mark"></span>
      <span class="brand-name">Quilvo<br>Garage Doors</span>
    </div>
  </section>

  <section class="card card-front" aria-label="Business card front">
    <div class="front-top">
      <div class="brand">
        <span class="brand-mark"></span>
        <span class="brand-name">Quilvo<br>Garage Doors</span>
      </div>
      <div class="person">
        <p class="person-name">Maren Holloway</p>
        <p class="person-role">General Manager</p>
      </div>
    </div>
    <div class="front-bottom">
      <ul class="contact-list">
        <li class="contact-item">
          <svg class="contact-icon" viewBox="0 0 18 18" aria-hidden="true"><rect width="18" height="18" rx="3" fill="var(--teal)"/><path d="M5.5 4.5h2l1 2.5-1.3 1a6 6 0 0 0 2.8 2.8l1-1.3 2.5 1v2a1 1 0 0 1-1 1A8.5 8.5 0 0 1 4.5 5.5a1 1 0 0 1 1-1z" fill="var(--card-dark)"/></svg>
          855-3-QUILVO
        </li>
        <li class="contact-item">
          <svg class="contact-icon" viewBox="0 0 18 18" aria-hidden="true"><rect width="18" height="18" rx="3" fill="var(--teal)"/><rect x="4" y="5.5" width="10" height="7" rx="1" fill="none" stroke="var(--card-dark)" stroke-width="1.4"/><path d="M4.5 6l4.5 3.5L13.5 6" fill="none" stroke="var(--card-dark)" stroke-width="1.4"/></svg>
          service@quilvogaragedoors.com
        </li>
        <li class="contact-item">
          <svg class="contact-icon" viewBox="0 0 18 18" aria-hidden="true"><rect width="18" height="18" rx="3" fill="var(--teal)"/><circle cx="9" cy="9" r="5" fill="none" stroke="var(--card-dark)" stroke-width="1.3"/><ellipse cx="9" cy="9" rx="2.2" ry="5" fill="none" stroke="var(--card-dark)" stroke-width="1.1"/><path d="M4 9h10" stroke="var(--card-dark)" stroke-width="1.1"/></svg>
          www.quilvogaragedoors.com
        </li>
      </ul>
      <div class="accent-stripe"></div>
    </div>
  </section>
</main>
</body>
</html>
```